Customizing and design a blog from the scratch

I need a blog designer to customize my blog from scratch, I have create the blog with Wordpress with Divi theme but I have nothing to do with the layout and the design, I can only provide the menu list I have in my mind and the skill of writing,I need a talented blog designer to help me with that.Thanks

Colors

Designer to choose colors to be used in the design.

Requirements
Nice to have
• My blog name is
• Follow the quiet river
• So I would like an inspiring background, the blog will be having 5 main pages
• 1. Education
• 2.Kids corner
• 3.Health and fitness
• 4.Beauty and fashion
• 5.Arabian corner
• UNDER each of them I will post a daily new post.
• I would like to have a home page which side will write a brief post a bout the page.
• Hope that helps!

```html
<!DOCTYPE html>
<html lang="en">
<head>
<meta charset="utf-8">
<title>Follow the quiet river — Blog</title>
<link rel="stylesheet" href="https://fonts.googleapis.com/css2?family=Rubik:wght@500;700;900&family=Lato:wght@400;700&display=swap">
<style>
:root{
  --red:#e8371f;
  --orange:#f7a21b;
  --ink:#1c1c1c;
  --text:#2a2a2a;
  --muted:#7a7a7a;
  --line:#e4e4e4;
  --panel:#f4f4f4;
  --footer:#151515;
  --white:#ffffff;
  --fb:#2d4f9a;
  --tw:#1da1f2;
  --ig:#4a3b33;
}
*{box-sizing:border-box;margin:0;padding:0}
html,body{width:1200px;height:4000px;overflow:hidden}
body{position:relative;background:var(--white);font-family:"Lato",sans-serif;color:var(--text)}

/* hero */
.hero{position:absolute;left:0;top:0;width:1200px;height:670px;overflow:hidden}
.hero-photo{position:absolute;inset:0;background:
  radial-gradient(ellipse at 28% 40%,#c2704e 0,#8a4a2c 22%,transparent 45%),
  linear-gradient(100deg,#4d5a26 0%,#6b6a2e 30%,#7a4a26 60%,#3b2416 100%)}
.hero-shade{position:absolute;inset:0;background:linear-gradient(90deg,rgba(0,0,0,0) 40%,rgba(20,10,5,.45) 100%)}
.hero-wave{position:absolute;left:0;top:0}
.brand{position:absolute;left:144px;top:36px;display:flex;align-items:center;gap:12px}
.brand-mark{width:40px;height:40px;border-radius:50%;background:var(--orange)}
.brand-name{font-family:"Rubik",sans-serif;font-weight:700;font-size:26px;color:var(--white);text-transform:uppercase;letter-spacing:.3px;white-space:nowrap}
.nav{position:absolute;top:52px;left:632px;display:flex;gap:33px;font-family:"Lato",sans-serif;font-weight:700;font-size:15px;color:var(--white);text-transform:uppercase;white-space:nowrap}
.nav .active{color:var(--orange);border-bottom:3px solid var(--orange);padding-bottom:6px}
.hero-title{position:absolute;left:608px;top:200px;font-family:"Rubik",sans-serif;font-weight:900;font-size:66px;line-height:70px;color:var(--white);text-transform:uppercase;letter-spacing:1px;white-space:nowrap}
.btn{display:inline-flex;align-items:center;justify-content:center;gap:7px;background:var(--red);color:var(--white);font-weight:700;text-transform:uppercase;border-radius:30px;white-space:nowrap}
.btn .arr{width:12px;height:12px;border-radius:50%;background:var(--white);position:relative}
.btn .arr::after{content:"";position:absolute;left:3px;top:3px;border:3px solid transparent;border-left:5px solid var(--red)}
.hero-btn{position:absolute;left:608px;top:376px;width:179px;height:45px;font-size:15px}
.dots{position:absolute;left:1133px;top:273px;display:flex;flex-direction:column;gap:11px}
.dots span{width:11px;height:11px;border-radius:50%;background:var(--white)}
.dots .on{background:transparent;border:2px solid var(--white)}

/* main column */
.blog-head{position:absolute;left:144px;top:735px;width:613px;height:67px;border-bottom:1px solid var(--line);font-family:"Rubik",sans-serif;font-weight:900;font-size:40px;color:var(--ink)}
.category{position:absolute;left:144px;width:613px;height:496px}
.category h2{font-family:"Rubik",sans-serif;font-weight:700;font-size:26px;color:var(--red);text-transform:uppercase;line-height:28px;white-space:nowrap}
.feature{position:absolute;left:0;top:46px;width:275px;height:354px;background:var(--white);box-shadow:0 2px 8px rgba(0,0,0,.12)}
.feature .photo{height:175px}
.feature .avatar{position:absolute;left:25px;top:200px;width:26px;height:26px;border-radius:50%;background:#8d7a70}
.feature h3{position:absolute;left:64px;top:196px;width:200px;font-size:17px;line-height:21px;font-weight:700;color:var(--ink)}
.feature p{position:absolute;left:24px;top:253px;width:235px;font-size:11.5px;line-height:18px;color:var(--muted)}
.feature .meta{position:absolute;left:24px;top:322px;font-size:11.5px;color:var(--ink);display:flex;gap:8px;align-items:center;white-space:nowrap}
.ico-cal{width:10px;height:10px;border:2px solid var(--orange);border-radius:2px;display:inline-block}
.ico-chat{width:10px;height:8px;background:var(--orange);border-radius:4px;display:inline-block}
.post{position:absolute;left:301px;width:300px;height:95px}
.post .thumb{position:absolute;left:0;top:0;width:120px;height:95px}
.post h4{position:absolute;left:137px;top:10px;width:160px;font-size:17px;line-height:24px;font-weight:700;color:var(--ink)}
.post .date{position:absolute;left:137px;top:68px;font-size:11.5px;color:var(--orange);display:flex;gap:6px;align-items:center;white-space:nowrap}
.view-more{position:absolute;left:301px;top:386px;font-size:15px;font-weight:700;color:var(--red);text-transform:uppercase}
.share{position:absolute;left:0;top:444px;width:613px;height:49px;border-top:1px solid var(--line);border-bottom:1px solid var(--line)}
.share .label{position:absolute;left:22px;top:16px;font-size:16px;font-weight:700;color:var(--ink);text-transform:uppercase;white-space:nowrap}
.share .icons{position:absolute;left:130px;top:12px;display:flex;gap:5px}
.share .icons span{width:27px;height:27px;border-radius:50%}
.share .btn{position:absolute;left:447px;top:7px;width:143px;height:36px;font-size:14px}

.pager{position:absolute;left:144px;top:3530px;display:flex;align-items:center;font-size:13px;color:var(--ink)}
.pager span{width:36px;height:32px;display:flex;align-items:center;justify-content:center}
.pager .current{background:var(--orange);color:var(--white)}

/* sidebar */
.side-box{position:absolute;left:784px;width:272px;background:var(--panel);box-shadow:0 1px 6px rgba(0,0,0,.12)}
.side-box h3{font-family:"Lato",sans-serif;font-weight:700;font-size:31px;line-height:36px;color:var(--ink);text-transform:uppercase;white-space:nowrap}
.search{background:var(--white);top:743px;height:131px}
.search h4{position:absolute;left:20px;top:26px;font-size:19px;font-weight:700;color:var(--ink)}
.search .field{position:absolute;left:20px;top:61px;width:232px;height:40px;border:1px solid #cfcfcf;border-radius:20px;font-size:12px;color:var(--muted);padding:12px 19px}
.search .go{position:absolute;right:6px;top:7px;width:26px;height:26px;border-radius:50%;background:var(--red)}
.about{top:895px;height:280px;padding:30px 22px}
.about p{margin-top:16px;font-size:12.5px;line-height:26px;color:var(--muted)}
.about a{display:block;margin-top:12px;font-size:13px;font-weight:700;color:var(--red);text-decoration:none}
.news{top:1197px;height:433px;padding:30px 22px}
.news-item{position:absolute;left:23px;width:240px;height:86px}
.news-item .pic{position:absolute;left:0;top:0;width:86px;height:86px;border-radius:50%}
.news-item h4{position:absolute;left:95px;top:5px;width:140px;font-size:18px;line-height:24px;font-weight:700;color:var(--ink)}
.news-item .date{position:absolute;left:95px;top:58px;font-size:11px;color:var(--orange);display:flex;gap:5px;align-items:center;white-space:nowrap}
.letter{top:1651px;height:253px;padding:28px 22px}
.letter .input{position:absolute;left:23px;width:221px;height:36px;background:var(--white);border:1px solid #e6e6e6;font-size:12px;color:var(--muted);padding:11px 18px}
.letter .signup{position:absolute;left:23px;top:185px;width:221px;height:38px;background:var(--red);color:var(--white);font-size:14px;font-weight:700;display:flex;align-items:center;justify-content:center}
.social{top:1928px;height:225px;padding:24px 10px 24px 28px}
.social h3{font-size:30px}
.social .dots-grid{position:absolute;left:30px;top:82px;display:grid;grid-template-columns:repeat(3,47px);gap:19px 19px}
.social .dots-grid span{width:47px;height:47px;border-radius:50%}

/* footer */
.footer-wave{position:absolute;left:0;top:3555px}
.footer{position:absolute;left:0;top:3694px;width:1200px;height:306px;background:var(--footer);color:var(--white)}
.footer h5{font-size:17px;font-weight:700;text-transform:uppercase;line-height:21px}
.f-about{position:absolute;left:144px;top:54px;width:270px}
.f-about p{margin-top:16px;font-size:12px;line-height:23px}
.f-support{position:absolute;left:445px;top:54px}
.f-support ul{list-style:none;margin-top:16px;font-size:12px;line-height:28px}
.f-news{position:absolute;left:688px;top:54px;width:380px}
.f-news .mail{position:absolute;left:0;top:66px;width:248px;height:32px;border-bottom:1px solid #8a8a8a;font-size:9px;padding-top:8px}
.f-news .send{position:absolute;left:248px;top:66px;width:88px;height:32px;background:var(--orange);font-size:13px;font-weight:700;display:flex;align-items:center;justify-content:center}
.f-news .links{position:absolute;left:0;top:124px;display:flex;gap:26px}
.f-news .links span{width:18px;height:18px;border-radius:50%;background:var(--white)}
.copyright{position:absolute;left:0;top:260px;width:1200px;height:46px;border-top:1px solid #2c2c2c;background:#101010;font-size:12px;display:flex;align-items:center;justify-content:center}
</style>
</head>
<body>

<header class="hero">
  <div class="hero-photo" role="img" aria-label="Photo of a young woman in a coral sports top drinking from a water bottle in a sunlit forest, with a towel over her shoulder"></div>
  <div class="hero-shade"></div>
  <svg class="hero-wave" width="1200" height="670" viewBox="0 0 1200 670" aria-hidden="true">
    <path d="M0 560 C160 690 380 660 620 600 C860 540 1040 510 1200 585 L1200 670 L0 670 Z" fill="var(--orange)"/>
    <path d="M0 600 C170 700 400 680 640 620 C880 560 1050 545 1200 600 L1200 670 L0 670 Z" fill="var(--white)"/>
  </svg>
  <div class="brand"><span class="brand-mark"></span><span class="brand-name">Follow the quiet river</span></div>
  <nav class="nav"><span class="active">Home</span><span>About Us</span><span>Services</span><span>News</span><span>Contact</span></nav>
  <h1 class="hero-title">Follow the<br>quiet river</h1>
  <a class="btn hero-btn">Get Started <span class="arr"></span></a>
  <div class="dots"><span></span><span></span><span class="on"></span><span></span><span></span></div>
</header>

<h2 class="blog-head">BLOG</h2>

<section class="category" style="top:826px">
  <h2>Education</h2>
  <article class="feature">
    <div class="photo" role="img" aria-label="Photo of a smiling student with a stack of books in front of a chalkboard" style="background:linear-gradient(160deg,#5d6a68,#8a7a62 60%,#4d4a40)"></div>
    <span class="avatar"></span>
    <h3>Lorem ipsum dolor sit amet conseactetur</h3>
    <p>Sed ut perspiciatis unde omnis iste natus error sit voluptatem accusantium</p>
    <div class="meta"><i class="ico-cal"></i>Aug 31,2019 &nbsp;| &nbsp;<i class="ico-chat"></i>1</div>
  </article>
  <div class="post" style="top:46px"><div class="thumb" role="img" aria-label="Photo of children raising hands in a classroom" style="background:linear-gradient(135deg,#c9a98a,#e3cdb6)"></div><h4>Lorem ipsum dolor sit amet</h4><span class="date"><i class="ico-cal"></i>Aug 31,2019</span></div>
  <div class="post" style="top:155px"><div class="thumb" role="img" aria-label="Photo of a rocket drawn on a blackboard" style="background:linear-gradient(135deg,#2f3a44,#4b5560)"></div><h4>Lorem ipsum dolor sit amet</h4><span class="date"><i class="ico-cal"></i>Aug 31,2019</span></div>
  <div class="post" style="top:262px"><div class="thumb" role="img" aria-label="Photo of a teacher in a classroom" style="background:linear-gradient(135deg,#9a8670,#d8c6a8)"></div><h4>Lorem ipsum dolor sit amet</h4><span class="date"><i class="ico-cal"></i>Aug 31,2019</span></div>
  <a class="view-more">View More</a>
  <div class="share"><span class="label">Share On</span><div class="icons"><span style="background:var(--fb)"></span><span style="background:var(--tw)"></span><span style="background:var(--ig)"></span></div><a class="btn">Comment <span class="arr"></span></a></div>
</section>

<section class="category" style="top:1362px">
  <h2>Kids Corner</h2>
  <article class="feature">
    <div class="photo" role="img" aria-label="Photo of a laughing toddler playing with colourful building blocks" style="background:linear-gradient(160deg,#dfe8ee,#f2e6d6 60%,#d9a45a)"></div>
    <span class="avatar"></span>
    <h3>Lorem ipsum dolor sit amet conseactetur</h3>
    <p>Sed ut perspiciatis unde omnis iste natus error sit voluptatem accusantium</p>
    <div class="meta"><i class="ico-cal"></i>Aug 31,2019 &nbsp;| &nbsp;<i class="ico-chat"></i>1</div>
  </article>
  <div class="post" style="top:46px"><div class="thumb" role="img" aria-label="Photo of children running on grass" style="background:linear-gradient(135deg,#5f8a3c,#b58a5a)"></div><h4>Lorem ipsum dolor sit amet</h4><span class="date"><i class="ico-cal"></i>Aug 31,2019</span></div>
  <div class="post" style="top:155px"><div class="thumb" role="img" aria-label="Photo of a group of smiling children" style="background:linear-gradient(135deg,#6a4a36,#a57a5c)"></div><h4>Lorem ipsum dolor sit amet</h4><span class="date"><i class="ico-cal"></i>Aug 31,2019</span></div>
  <div class="post" style="top:262px"><div class="thumb" role="img" aria-label="Photo of a boy in goggles in a swimming pool" style="background:linear-gradient(135deg,#1f8fc4,#66c6e8)"></div><h4>Lorem ipsum dolor sit amet</h4><span class="date"><i class="ico-cal"></i>Aug 31,2019</span></div>
  <a class="view-more">View More</a>
  <div class="share"><span class="label">Share On</span><div class="icons"><span style="background:var(--fb)"></span><span style="background:var(--tw)"></span><span style="background:var(--ig)"></span></div><a class="btn">Comment <span class="arr"></span></a></div>
</section>

<section class="category" style="top:1898px">
  <h2>Health and Fitness</h2>
  <article class="feature">
    <div class="photo" role="img" aria-label="Photo of a woman in a gym holding a red apple" style="background:linear-gradient(160deg,#8c8c8c,#3a3230 60%,#6b5a52)"></div>
    <span class="avatar"></span>
    <h3>Lorem ipsum dolor sit amet conseactetur</h3>
    <p>Sed ut perspiciatis unde omnis iste natus error sit voluptatem accusantium</p>
    <div class="meta"><i class="ico-cal"></i>Aug 31,2019 &nbsp;| &nbsp;<i class="ico-chat"></i>1</div>
  </article>
  <div class="post" style="top:46px"><div class="thumb" role="img" aria-label="Photo of a bowl of fresh fruit" style="background:linear-gradient(135deg,#c2392a,#6f9a32)"></div><h4>Lorem ipsum dolor sit amet</h4><span class="date"><i class="ico-cal"></i>Aug 31,2019</span></div>
  <div class="post" style="top:155px"><div class="thumb" role="img" aria-label="Photo of a cheerful woman in a white top" style="background:linear-gradient(135deg,#d9a88a,#f1e4da)"></div><h4>Lorem ipsum dolor sit amet</h4><span class="date"><i class="ico-cal"></i>Aug 31,2019</span></div>
  <div class="post" style="top:262px"><div class="thumb" role="img" aria-label="Photo of a runner tying her shoes" style="background:linear-gradient(135deg,#c9773c,#e6b07a)"></div><h4>Lorem ipsum dolor sit amet</h4><span class="date"><i class="ico-cal"></i>Aug 31,2019</span></div>
  <a class="view-more">View More</a>
  <div class="share"><span class="label">Share On</span><div class="icons"><span style="background:var(--fb)"></span><span style="background:var(--tw)"></span><span style="background:var(--ig)"></span></div><a class="btn">Comment <span class="arr"></span></a></div>
</section>

<section class="category" style="top:2434px">
  <h2>Beauty and Fashion</h2>
  <article class="feature">
    <div class="photo" role="img" aria-label="Beauty portrait of a woman with clear skin" style="background:linear-gradient(160deg,#e9dcd3,#d7b8a4 60%,#efe4dc)"></div>
    <span class="avatar"></span>
    <h3>Lorem ipsum dolor sit amet conseactetur</h3>
    <p>Sed ut perspiciatis unde omnis iste natus error sit voluptatem accusantium</p>
    <div class="meta"><i class="ico-cal"></i>Aug 31,2019 &nbsp;| &nbsp;<i class="ico-chat"></i>1</div>
  </article>
  <div class="post" style="top:46px"><div class="thumb" role="img" aria-label="Photo of a woman receiving a facial mask treatment" style="background:linear-gradient(135deg,#efe6e0,#d9b9a8)"></div><h4>Lorem ipsum dolor sit amet</h4><span class="date"><i class="ico-cal"></i>Aug 31,2019</span></div>
  <div class="post" style="top:155px"><div class="thumb" role="img" aria-label="Fashion photo of a woman in a hat and sunglasses" style="background:linear-gradient(135deg,#e8e2d8,#b59a7a)"></div><h4>Lorem ipsum dolor sit amet</h4><span class="date"><i class="ico-cal"></i>Aug 31,2019</span></div>
  <div class="post" style="top:262px"><div class="thumb" role="img" aria-label="Fashion photo of a woman in a black jacket" style="background:linear-gradient(135deg,#f1f1f1,#3a3a3a)"></div><h4>Lorem ipsum dolor sit amet</h4><span class="date"><i class="ico-cal"></i>Aug 31,2019</span></div>
  <a class="view-more">View More</a>
  <div class="share"><span class="label">Share On</span><div class="icons"><span style="background:var(--fb)"></span><span style="background:var(--tw)"></span><span style="background:var(--ig)"></span></div><a class="btn">Comment <span class="arr"></span></a></div>
</section>

<section class="category" style="top:2970px">
  <h2>Arabian Corner</h2>
  <article class="feature">
    <div class="photo" role="img" aria-label="Photo of a grand white mosque lit up at dusk" style="background:linear-gradient(180deg,#e59a8a,#b06a8a 55%,#6a4a7a)"></div>
    <span class="avatar"></span>
    <h3>Lorem ipsum dolor sit amet conseactetur</h3>
    <p>Sed ut perspiciatis unde omnis iste natus error sit voluptatem accusantium</p>
    <div class="meta"><i class="ico-cal"></i>Aug 31,2019 &nbsp;| &nbsp;<i class="ico-chat"></i>1</div>
  </article>
  <div class="post" style="top:46px"><div class="thumb" role="img" aria-label="Photo of a glowing Arabian lantern" style="background:linear-gradient(135deg,#4a1a5a,#b03a9a)"></div><h4>Lorem ipsum dolor sit amet</h4><span class="date"><i class="ico-cal"></i>Aug 31,2019</span></div>
  <div class="post" style="top:155px"><div class="thumb" role="img" aria-label="Night sky over a mosque silhouette" style="background:linear-gradient(135deg,#0f1e4a,#2a4a8a)"></div><h4>Lorem ipsum dolor sit amet</h4><span class="date"><i class="ico-cal"></i>Aug 31,2019</span></div>
  <div class="post" style="top:262px"><div class="thumb" role="img" aria-label="Blue glowing ornamental artwork" style="background:linear-gradient(135deg,#050a1e,#1f5aa8)"></div><h4>Lorem ipsum dolor sit amet</h4><span class="date"><i class="ico-cal"></i>Aug 31,2019</span></div>
  <a class="view-more">View More</a>
  <div class="share"><span class="label">Share On</span><div class="icons"><span style="background:var(--fb)"></span><span style="background:var(--tw)"></span><span style="background:var(--ig)"></span></div><a class="btn">Comment <span class="arr"></span></a></div>
</section>

<nav class="pager"><span>&larr;</span><span>01</span><span class="current">02</span><span>03</span><span>04</span><span>09</span><span>&rarr;</span></nav>

<aside>
  <div class="side-box search">
    <h4>Search</h4>
    <div class="field">Search..<span class="go"></span></div>
  </div>
  <div class="side-box about">
    <h3>About Us</h3>
    <p>Neim ipsam voluptatem quia voluptas sit aspernatur aut odit aut fugit, sed quia consequuntur mamvoluptatem quia voluptas sit aspernatur aut odit aut f qquuntur magni.</p>
    <a>READ MORE &#10140;</a>
  </div>
  <div class="side-box news">
    <h3>Latest News</h3>
    <div class="news-item" style="top:88px"><div class="pic" role="img" aria-label="Photo of fresh fruit" style="background:linear-gradient(135deg,#c2392a,#6f9a32)"></div><h4>Lorem ipsum dolor sit amet</h4><span class="date"><i class="ico-cal"></i>Aug 31,2019</span></div>
    <div class="news-item" style="top:195px"><div class="pic" role="img" aria-label="Photo of a woman exercising with a rope" style="background:linear-gradient(135deg,#3a3a3a,#b08a70)"></div><h4>Lorem ipsum dolor sit amet</h4><span class="date"><i class="ico-cal"></i>Aug 31,2019</span></div>
    <div class="news-item" style="top:304px"><div class="pic" role="img" aria-label="Photo of children in a classroom" style="background:linear-gradient(135deg,#c9a98a,#e3cdb6)"></div><h4>Lorem ipsum dolor sit amet</h4><span class="date"><i class="ico-cal"></i>Aug 31,2019</span></div>
  </div>
  <div class="side-box letter">
    <h3>Newsletter</h3>
    <div class="input" style="top:83px">Enter Name</div>
    <div class="input" style="top:134px">Enter Email</div>
    <div class="signup">SIGN UP</div>
  </div>
  <div class="side-box social">
    <h3>Social Media</h3>
    <div class="dots-grid">
      <span style="background:#3b5998"></span><span style="background:#2b2b2b"></span><span style="background:#d7263d"></span>
      <span style="background:#8cc63f"></span><span style="background:#1a6fa8"></span><span style="background:#2aa3ef"></span>
    </div>
  </div>
</aside>

<svg class="footer-wave" width="1200" height="140" viewBox="0 0 1200 140" aria-hidden="true">
  <path d="M0 115 C250 155 520 110 760 60 C950 20 1100 0 1200 10 L1200 140 L0 140 Z" fill="var(--orange)"/>
  <path d="M0 130 C260 165 540 125 780 80 C970 45 1110 30 1200 40 L1200 140 L0 140 Z" fill="var(--footer)"/>
</svg>

<footer class="footer">
  <div class="f-about">
    <h5>About Us</h5>
    <p>Lorem ipsum dolor sit amet, conse adipisicing elit, sed do eiusmod tempor incididunt ut labore dolore magna aliqua.</p>
  </div>
  <div class="f-support">
    <h5>Customer Support</h5>
    <ul><li>Terms and conditions</li><li>Privacy Policy</li><li>FAQ</li><li>Sitemap</li><li>Contact Us</li></ul>
  </div>
  <div class="f-news">
    <h5>Sign up for our newsletter to receive exclusive discounts &amp; offers!</h5>
    <div class="mail">Enter Email Address</div>
    <div class="send">SIGN UP</div>
    <div class="links"><span></span><span></span><span></span><span></span></div>
  </div>
  <div class="copyright">Copyright 2019 &nbsp;Follow the quiet river. All Rights Reserved</div>
</footer>

</body>
</html>
```